Commit to H.E.A.L. (Healthy Eating and Living)Corporate Wellness

Rise with B.R.I.G.H.T. (Balanced Habits In Good Routines Today) is my health and wellness company. I am a certified Health & Lifestyle Coach who provides a 6 month one-on-one coaching program for individuals and groups. I also provide 1 hour health seminars or "brown bag" lunches for any type of organization. My focus is on prevention of chronic disease through health and food education, as well as effective lifestyle coaching. I would like the brochure to have my logo, my name and certification, some health statistics, and my programs/seminars. Looking for a one page, half fold or trifold brochure design. I am flexible! I forgot to include my personal information. phone number 555/314-0872. email is marla@teachandthrivenation.example. website is www.risewithbright.example.

Target Market(s)

Companies (large or small) looking for wellness and disease prevention programs for their employees.

Industry/Entity Type

Health

Requirements
Must have
• I am going into this with no picture in my head as to what I want. I like simplicity. I like to represent health, in all aspects, from food to environment. I will attach my logo to use, and colors should accent the logo.
I need it to include my name and title (Marla Vesterling, Certified Health & Lifestyle Coach). The tag line "Because your workforce's wellbeing IS your bottom line." These statistics listed clearly: "1. The U.S. spends $2.8 trillion on health care every year, and this number is rising. 2. Treating individuals with chronic preventable disease is responsible for 75% of our health care costs. 3. The U.S. spends more on healthcare than Japan, Germany, France, China, UK, Italy, Canada, Brazil, Spain and Australia COMBINED. 4. The Global Vitality Council ranks the U.S. 37th for overall health outcomes. This means that more healthcare spending does not equate to better health.
Then it needs to say that "Our healthcare costs are out of control, increasing, and unsustainable. We do not have a healthcare system, we have a disease care system. Prevention of chronic disease is the only way to reduce our costs. Workplace wellness solutions MUST change behaviors. Food and health education, as well as effective lifestyle coaching are the keys to this behavior change."
I offer 1 hour seminars, sample seminars include but are not limited to "Tumor Avoidance" "Nation's Plate/Nation's Ailment," and "Vitality & Balance starts when Old Routines Stop." I also offer a six month bi-weekly health coaching program for individuals or small groups. Plus custom programs that include health food store tours, pantry purges, cooking ideas and preparation, etc.

```html
<!DOCTYPE html>
<html lang="en">
<head>
<meta charset="utf-8">
<title>Rise with B.R.I.G.H.T. – Corporate Wellness Brochure</title>
<link rel="stylesheet" href="https://fonts.googleapis.com/css2?family=Open+Sans:ital,wght@0,400;0,600;1,400&family=Arimo:ital,wght@0,400;1,400&display=swap">
<style>
  :root {
    --brand-green: #6fe000;
    --heading-green: #7ccf1e;
    --accent-green: #86d42a;
    --text-dark: #2b2b2b;
    --panel-light: #ffffff;
    --panel-tint: #e9f6dc;
    --divider: #d9ecc7;
    --mark-top: #b9e07e;
    --mark-bottom: #e6f4d2;
    --photo-top: #f6f0f4;
    --photo-mid: #ecd2e4;
    --photo-low: #dfe9e2;
  }
  * { box-sizing: border-box; margin: 0; padding: 0; }
  html, body { width: 1200px; height: 930px; overflow: hidden; background: #fff; }
  .brochure {
    position: relative;
    width: 1200px; height: 930px;
    overflow: hidden;
    font-family: "Arimo", Arial, sans-serif;
    color: var(--text-dark);
  }
  .band { position: absolute; left: 0; width: 1200px; background: var(--brand-green); }
  .band--top { top: 0; height: 22px; }
  .band--bottom { bottom: 0; height: 24px; }
  .panel { position: absolute; top: 22px; bottom: 24px; }
  .panel--left {
    left: 0; width: 617px;
    background: linear-gradient(180deg, #eef8e4 0%, var(--panel-light) 45%, #f3faec 100%);
  }
  .panel--right {
    left: 619px; width: 581px;
    background: linear-gradient(180deg, #f1f9e9 0%, #ffffff 40%, var(--panel-tint) 100%);
    border-left: 2px solid var(--divider);
  }
  .brand-mark {
    position: absolute;
    width: 62px; height: 88px;
    border-radius: 4px;
    background: linear-gradient(180deg, var(--mark-top) 0%, var(--mark-bottom) 100%);
  }
  .panel--left .brand-mark { left: 95px; top: 76px; }
  .panel--right .brand-mark { left: 49px; top: 82px; }
  .headline {
    position: absolute;
    font-family: "Open Sans", sans-serif;
    font-weight: 400;
    color: var(--heading-green);
    line-height: 1.02;
  }
  .panel--left .headline { left: 160px; top: 86px; font-size: 30px; width: 430px; }
  .panel--right .headline { left: 124px; top: 80px; font-size: 31px; width: 385px; }
  .stats {
    position: absolute; left: 90px; top: 188px; width: 460px;
    font-size: 14px; line-height: 17px;
    padding-left: 24px;
  }
  .stats li { margin-bottom: 8px; padding-left: 2px; }
  .team-photo {
    position: absolute; left: 60px; top: 428px;
    width: 510px; height: 370px;
    background: linear-gradient(180deg, #eef3ee 0%, #c9cdd3 50%, #6b6f78 100%);
    border-radius: 4px;
  }
  .mission {
    position: absolute; left: 62px; top: 193px; width: 455px;
    font-family: "Open Sans", sans-serif;
    font-size: 13px; line-height: 18px;
  }
  .savings-photo {
    position: absolute; left: 170px; top: 283px;
    width: 290px; height: 280px;
    border-radius: 4px;
    background: linear-gradient(180deg, var(--photo-top) 0%, var(--photo-mid) 45%, var(--photo-low) 100%);
  }
  .services {
    position: absolute; left: 41px; top: 604px; width: 505px;
    font-style: italic; font-size: 13px; line-height: 21px;
    color: var(--accent-green);
  }
  .coach-name {
    position: absolute; left: 136px; top: 752px;
    font-family: "Open Sans", sans-serif;
    font-size: 36px; font-weight: 400;
    color: var(--accent-green);
  }
  .coach-title {
    position: absolute; left: 148px; top: 806px;
    font-family: "Open Sans", sans-serif;
    font-size: 17px; color: var(--text-dark);
  }
</style>
</head>
<body>
<main class="brochure">
  <div class="band band--top"></div>

  <section class="panel panel--left">
    <div class="brand-mark" role="img" aria-label="Company logo symbol"></div>
    <h1 class="headline">Because your workforce's wellbeing IS your bottom line</h1>
    <ol class="stats">
      <li>The U.S. spends $2.8 trillion on health care every year, and this number is rising.</li>
      <li>Treating individuals with chronic preventable disease is responsible for 75% of our health care costs.</li>
      <li>The U.S. spends more on healthcare than Japan, Germany, France, China, UK, Italy, Canada, Brazil, Spain and Australia COMBINED.</li>
      <li>The Global Vitality Council ranks the U.S. 37th for overall health outcomes. This means that more healthcare spending does not equate to better health.</li>
    </ol>
    <div class="team-photo" role="img" aria-label="Photo of five cheering business people in suits with arms raised"></div>
  </section>

  <section class="panel panel--right">
    <div class="brand-mark" role="img" aria-label="Company logo symbol"></div>
    <h2 class="headline">Our healthcare costs are out of control, increasing, and unsustainable</h2>
    <p class="mission">We do not have a healthcare system, we have a disease care system. Prevention of chronic disease is the only way to reduce our costs. Workplace wellness solutions MUST change behaviors. Food and health education, as well as effective lifestyle coaching are the keys to this behavior change."</p>
    <div class="savings-photo" role="img" aria-label="Photo of a pink piggy bank wearing a green surgical mask"></div>
    <p class="services">I offer 1 hour seminars, sample seminars include but are not limited to "Tumor Avoidance" "Nation's Plate/Nation's Ailment," and "Vitality &amp; Balance starts when Old Routines Stop." I also offer a six month bi-weekly health coaching program for individuals or small groups. Plus custom programs that include health food store tours, pantry purges, cooking ideas and preparation, etc.</p>
    <p class="coach-name">Marla Vesterling</p>
    <p class="coach-title">Certified Health Lifestyle Coach</p>
  </section>

  <div class="band band--bottom"></div>
</main>
</body>
</html>
```